Redesign of an existing webpage

We've just redesigned our logo on a new website design to reflect the new logo. That wants to change the color and graphical appearance of our website. There are no restrictions on what should be changed. IT should display our portfolio and pricing and explain our product. Please provide stock photos if needed. The site structure should not be changed. So we want the pages which are currently there. We need the following pages: Main page (Home page) Detail page (currently used at AGB and questions) Imprint (including the map) existing webpage: www.plorvane.de
Updates

I've got a request from one of the designers-

Target Market(s)

We are offering IT services to small companies. The do not need own IT equipment or PC Specialists if if our service.

Industry/Entity Type

It Service

Coding

Coded - Design and coding required

Number of Pages Required

3 page

Font styles to use
Other font styles liked:
• Relaway

Colors

Designer to choose colors to be used in the design.

Requirements
Must have
• our login mask at https://desktop.plorvane.com needs a rebranding too

```html
<!DOCTYPE html>
<html lang="en">
<head>
<meta charset="utf-8">
<title>Plorvane – Just work.</title>
<link href="https://fonts.googleapis.com/css2?family=Raleway:wght@400;500;600;700&display=swap" rel="stylesheet">
<style>
:root{
  --blue:#1670d8;
  --blue-deep:#0b5bc2;
  --ink:#1f2226;
  --text:#9aa0a8;
  --line:#e8ebef;
  --pale:#f3f6f9;
  --footer:#1e2023;
  --white:#fff;
}
*{box-sizing:border-box;margin:0;padding:0}
html,body{width:1200px;height:4990px;overflow:hidden;background:var(--white)}
body{font-family:"Raleway",sans-serif;color:var(--ink)}
.page{position:relative;width:1200px;height:4990px;overflow:hidden}
.abs{position:absolute}
.accent{color:var(--blue)}
p.body{font-size:12px;line-height:18px;color:var(--text)}
.btn{position:absolute;display:flex;align-items:center;justify-content:center;border-radius:20px;font-size:9px;font-weight:700;letter-spacing:.6px;text-transform:uppercase}
.btn-solid{background:var(--blue);color:var(--white)}
.btn-line{border:2px solid var(--blue);color:var(--blue);background:var(--white)}
.brand{position:absolute;font-weight:700;font-size:24px;letter-spacing:3px;line-height:28px;display:flex;align-items:center;gap:10px;color:var(--blue)}
.brand i{display:block;width:14px;height:14px;background:var(--blue)}
h2.section{position:absolute;left:0;width:1200px;text-align:center;font-size:31px;font-weight:500}
/* hero */
.nav-login{left:815px;top:42px;font-size:9px;font-weight:700;color:var(--white);letter-spacing:1px}
.burger{left:1103px;top:42px;width:18px}
.burger span{display:block;height:2px;background:var(--white);margin-bottom:4px}
.hero-title{left:80px;top:180px;font-size:36px;font-weight:500}
.hero-text{left:80px;top:246px;width:360px}
.hero-text p+p{margin-top:18px}
/* cards */
.intro-card{left:157px;top:677px;width:886px;height:459px;background:var(--white);box-shadow:0 10px 40px rgba(20,40,70,.08)}
.intro-col{position:absolute;top:35px;width:265px}
.icon-ring{width:120px;height:120px;border-radius:50%;border:2px solid;display:flex;align-items:center;justify-content:center}
.intro-col h3{font-size:16px;font-weight:700;margin:28px 0 12px}
/* steps */
.steps{left:664px;top:1215px;width:327px;height:488px;background:var(--white);box-shadow:0 10px 40px rgba(20,40,70,.08)}
.step{position:absolute;left:24px;right:24px;height:86px;display:flex;align-items:center;gap:22px;border-bottom:1px solid var(--line);font-size:14px;font-weight:600}
.step-dot{width:48px;height:48px;border-radius:50%;background:var(--pale);display:flex;align-items:center;justify-content:center}
.step-active{left:611px;top:1325px;width:432px;height:159px;background:var(--white);box-shadow:0 14px 40px rgba(20,40,70,.14);display:flex;align-items:center;gap:24px;padding-left:24px}
.step-active .big{width:106px;height:106px;border-radius:50%;background:var(--blue);display:flex;align-items:center;justify-content:center;flex:none}
/* benefits */
.benefit{position:absolute;top:1784px;width:204px;height:267px;background:var(--white);border:1px solid var(--line);padding:24px 22px}
.benefit h4{font-size:14px;font-weight:700;margin:26px 0 10px}
.arrow-btn{position:absolute;top:2088px;width:38px;height:38px;border-radius:50%;border:2px solid var(--blue);display:flex;align-items:center;justify-content:center}
/* pricing */
.plan{position:absolute;top:2742px;width:357px;height:399px;background:var(--white);box-shadow:0 10px 40px rgba(20,40,70,.08)}
.plan-head{height:155px;background:linear-gradient(158deg,var(--blue) 0 50%,#3c3f45 50.2%);color:var(--white);position:relative}
.plan-head h5{position:absolute;left:56px;top:40px;font-size:16px;font-weight:600}
.plan-head .sq{position:absolute;left:24px;top:32px;width:24px;height:24px;border:3px solid var(--white)}
.plan-head .price{position:absolute;right:24px;top:82px;font-size:30px;font-weight:400}
.plan-head .per{position:absolute;right:24px;top:124px;font-size:11px}
.plan ul{list-style:none;padding:28px 24px 0}
.plan li{font-size:12px;color:var(--text);height:37px;border-bottom:1px solid var(--line);display:flex;align-items:center;gap:10px}
/* founder */
.founder{left:157px;top:3346px;width:886px;height:518px;background:var(--white);box-shadow:0 10px 40px rgba(20,40,70,.08)}
/* footer */
.footer{left:0;top:4586px;width:1200px;height:404px;background:var(--footer);color:#c9ccd1}
.footer h6{position:absolute;top:81px;font-size:13px;font-weight:600;color:var(--blue)}
.footer ul{position:absolute;top:117px;list-style:none;font-size:11px;line-height:19px;color:#d2d5da}
.footer ul li::before{content:"·";margin-right:8px}
.social{position:absolute;top:160px;width:30px;height:30px;border-radius:50%;border:1px solid var(--blue)}
</style>
</head>
<body>
<div class="page">

<!-- hero -->
<svg class="abs" style="left:0;top:0" width="1200" height="700" viewBox="0 0 1200 700" role="img" aria-label="Photo of a young woman working at a laptop in an office">
  <defs>
    <linearGradient id="heroPhoto" x1="0" y1="0" x2="1" y2="1">
      <stop offset="0" stop-color="#8f8a86"/><stop offset=".5" stop-color="#5d5f66"/><stop offset="1" stop-color="#2f3540"/>
    </linearGradient>
  </defs>
  <path d="M505 0 C540 60 585 120 590 200 C596 300 560 390 640 430 C740 470 900 420 1040 500 C1120 545 1170 610 1200 690 L1200 0 Z" fill="url(#heroPhoto)"/>
</svg>
<svg class="abs" style="left:0;top:515px" width="260" height="560" viewBox="0 0 260 560">
  <path d="M0 0 C120 10 220 70 250 70 C220 190 180 300 150 400 C110 500 50 540 0 550 Z" fill="var(--blue)"/>
</svg>

<div class="brand" style="left:80px;top:30px"><i></i>PLORVANE</div>
<div class="abs nav-login">LOG IN</div>
<div class="btn btn-solid" style="left:892px;top:32px;width:152px;height:30px">Get started now!</div>
<div class="abs burger"><span></span><span></span><span></span></div>
<svg class="abs" style="left:594px;top:412px" width="12" height="16" viewBox="0 0 12 16"><path d="M6 0v14M1 9l5 5 5-5" stroke="var(--blue)" stroke-width="1.5" fill="none"/></svg>

<h1 class="abs hero-title">Just <span class="accent">work.</span></h1>
<div class="abs hero-text">
  <p class="body">In large companies, IT departments ensure a functioning IT. Central servers are used, which are accessed from the individual workstations.</p>
  <p class="body">Plorvane has set itself the goal of providing such a solution to small and medium-sized companies at manageable costs.</p>
</div>
<div class="btn btn-line" style="left:80px;top:412px;width:160px;height:38px">Get started now!</div>
<div class="btn btn-solid" style="left:248px;top:412px;width:128px;height:38px">Learn more</div>

<!-- it that just works -->
<h2 class="section" style="top:600px">IT that <span class="accent">just works</span></h2>
<div class="abs intro-card">
  <div class="intro-col" style="left:22px">
    <div class="icon-ring" style="border-color:#e8403c">
      <svg width="56" height="56" viewBox="0 0 56 56"><ellipse cx="28" cy="32" rx="13" ry="16" fill="#e8403c"/><circle cx="28" cy="14" r="7" fill="#e8403c"/><path d="M6 24h12M6 34h10M8 46l10-6M50 24H38M50 34H40M48 46l-10-6" stroke="#e8403c" stroke-width="3"/></svg>
    </div>
    <h3>The problem</h3>
    <p class="body">The basis of the IT problems that unnecessarily complicate your daily business is - in addition to the human factor - the computer itself, because there are viruses landing programs are paralyzed and lost data</p>
  </div>
  <div class="intro-col" style="left:325px">
    <div class="icon-ring" style="border-color:#6cc04a">
      <svg width="56" height="56" viewBox="0 0 56 56"><rect x="10" y="14" width="24" height="24" rx="3" fill="#6cc04a"/><rect x="26" y="24" width="22" height="20" rx="3" fill="#4fa33a"/><circle cx="22" cy="12" r="5" fill="#6cc04a"/><circle cx="48" cy="32" r="5" fill="#4fa33a"/></svg>
    </div>
    <h3>Our solution</h3>
    <p class="body">Plorvane provides you with a solution that ensures the daily backup of your data and the monitoring of the operational readiness of your system. That's what we do at the base: everything you need to work on is moved to the servers in our data center. All necessary legal and other requirements are implemented by us.</p>
  </div>
  <div class="intro-col" style="left:628px">
    <div class="icon-ring" style="border-color:var(--blue)">
      <svg width="56" height="56" viewBox="0 0 56 56"><path d="M28 4 L48 12 V28 C48 40 38 48 28 52 C18 48 8 40 8 28 V12 Z" fill="var(--blue)"/><circle cx="40" cy="40" r="9" fill="#fff"/><path d="M35 40l4 4 6-7" stroke="var(--blue)" stroke-width="2.5" fill="none"/></svg>
    </div>
    <h3>Your safety</h3>
    <p class="body">If you're wondering how secure our solution is, the answer is simple: very safe. We work with Northgate, one of Germany's largest data centers. The security features of this data center are similar to those of a high-security system. Their data is protected against malicious software, unauthorized access and even natural disasters, and in the event of a power failure, generators and backup batteries ensure continuous operation.</p>
  </div>
</div>

<!-- become a customer -->
<h2 class="abs" style="left:157px;top:1376px;font-size:28px;font-weight:500;line-height:35px">How do I <span class="accent">become a<br>customer?</span></h2>
<p class="abs body" style="left:157px;top:1468px;width:310px">To become a Plorvane customer requires the following four steps.</p>
<div class="abs steps">
  <div class="step" style="top:0"><div class="step-dot"><svg width="20" height="14" viewBox="0 0 20 14"><path d="M1 7l4 4 8-9M7 11l2 1 9-10" stroke="var(--blue)" stroke-width="1.6" fill="none"/></svg></div>Select service</div>
  <div class="step" style="top:278px"><div class="step-dot"><svg width="14" height="16" viewBox="0 0 14 16"><path d="M0 0h9l5 5v11H0z" fill="var(--blue)"/><path d="M3 8h8M3 11h8" stroke="#fff"/></svg></div>Sign a contract</div>
  <div class="step" style="top:387px;border:0"><div class="step-dot"><svg width="16" height="16" viewBox="0 0 16 16"><rect y="2" width="16" height="14" rx="2" fill="var(--blue)"/><path d="M3 7h10M3 10h10M3 13h6" stroke="#fff"/></svg></div>Work loose</div>
</div>
<div class="abs step-active">
  <div class="big"><svg width="38" height="38" viewBox="0 0 24 24"><path d="M6.6 10.8a15 15 0 0 0 6.6 6.6l2.2-2.2c.3-.3.7-.4 1-.2 1.1.4 2.3.6 3.6.6.6 0 1 .4 1 1V20c0 .6-.4 1-1 1A17 17 0 0 1 3 4c0-.6.4-1 1-1h3.5c.6 0 1 .4 1 1 0 1.3.2 2.5.6 3.6.1.3 0 .7-.2 1z" fill="#fff"/><circle cx="15" cy="7" r="1" fill="#fff"/><circle cx="18" cy="7" r="1" fill="#fff"/><circle cx="21" cy="7" r="1" fill="#fff"/></svg></div>
  <div>
    <div style="font-size:14px;font-weight:600;margin-bottom:10px">Send an inquiry</div>
    <p class="body" style="width:268px">Fill out our form for a contract request without obligation. We evaluate the feasibility and draft a contract.</p>
  </div>
</div>

<!-- benefits -->
<svg class="abs" style="left:0;top:1700px" width="1200" height="920" viewBox="0 0 1200 920">
  <path d="M0 380 C250 350 420 200 620 120 C820 40 1000 60 1200 120 L1200 920 L0 920 Z" fill="var(--pale)"/>
</svg>
<h2 class="abs" style="left:80px;top:1792px;font-size:28px;font-weight:500;line-height:37px"><span class="accent">Your benefits</span> at a<br>glance!</h2>
<p class="abs body" style="left:80px;top:1880px;width:305px;font-size:11.5px">Explode resources for your core business because you do not have to worry about time-consuming malfunctions such as lame programs, virus attacks, data loss, etc., nor do you have to book an external service provider for rectification. Capacity and storage issues are a thing of the past, and your operating system is updated by the data center - faster, more direct, and much safer than what you could do on-site. If you use our ThinClients, further investments in your EDP infrastructure will be avoided.</p>
<div class="benefit" style="left:460px">
  <svg width="54" height="54" viewBox="0 0 54 54"><circle cx="27" cy="30" r="19" fill="none" stroke="#2b2f35" stroke-width="2"/><circle cx="27" cy="30" r="13" fill="none" stroke="var(--blue)" stroke-width="2"/><path d="M27 30V20M27 30l7 4M22 6h10M27 6v5" stroke="#2b2f35" stroke-width="2"/></svg>
  <h4>Express suppression</h4>
  <p class="body">Mondays to Fridays the troubleshooting is done in a maximum of 8 hours by the Plorvane Support evaluate the feasibility and draft a contract.</p>
</div>
<div class="benefit" style="left:687px">
  <svg width="54" height="54" viewBox="0 0 54 54"><rect x="3" y="6" width="48" height="40" rx="2" fill="none" stroke="#2b2f35" stroke-width="2"/><path d="M3 14h48" stroke="#2b2f35" stroke-width="2"/><circle cx="30" cy="32" r="8" fill="none" stroke="var(--blue)" stroke-width="2"/><path d="M10 22h10M10 28h8M10 34h8" stroke="#2b2f35" stroke-width="2"/></svg>
  <h4>Fast programs</h4>
  <p class="body">Our technology brings the maximum speed out of your existing applications</p>
</div>
<div class="benefit" style="left:913px">
  <svg width="54" height="54" viewBox="0 0 54 54"><rect x="3" y="4" width="40" height="40" rx="2" fill="none" stroke="#2b2f35" stroke-width="2"/><path d="M3 12h40M10 20h14M10 26h14M10 32h10" stroke="#2b2f35" stroke-width="2"/><rect x="32" y="30" width="18" height="16" rx="2" fill="none" stroke="var(--blue)" stroke-width="2"/><path d="M36 30v-5a5 5 0 0 1 10 0v5" fill="none" stroke="var(--blue)" stroke-width="2"/></svg>
  <h4>Data protection</h4>
  <p class="body">Our service includes professional protection against viruses, cryptoviruses, Trojans and other pests</p>
</div>
<div class="arrow-btn" style="left:745px"><svg width="8" height="12" viewBox="0 0 8 12"><path d="M6 1L1 6l5 5" stroke="var(--ink)" stroke-width="1.5" fill="none"/></svg></div>
<div class="arrow-btn" style="left:794px"><svg width="8" height="12" viewBox="0 0 8 12"><path d="M2 1l5 5-5 5" stroke="var(--ink)" stroke-width="1.5" fill="none"/></svg></div>

<!-- why -->
<div class="abs" style="left:180px;top:2206px;width:280px;height:330px;border:2px solid var(--blue)"></div>
<div class="abs" role="img" aria-label="Photo of three colleagues looking at a tablet together" style="left:157px;top:2231px;width:278px;height:327px;border-radius:8px;background:linear-gradient(135deg,#c9ccd0,#8e959e 60%,#6a7079)"></div>
<div class="abs" style="left:536px;top:2262px;font-size:9px;font-weight:700;letter-spacing:1px;color:var(--blue)">WHY PLORVANE</div>
<h2 class="abs" style="left:536px;top:2283px;font-size:29px;font-weight:500">Simple, <span class="accent">reliable and cheap</span></h2>
<p class="abs body" style="left:536px;top:2346px;width:480px">Big companies have been working this way for years, cutting costs and improving stability. Now Plorvane offers the solution for even the smallest businesses. We store your data permanently in a safe place. Necessary security measures are taken, your data is backed up and you focus on your daily business.</p>
<div class="btn btn-solid" style="left:536px;top:2467px;width:130px;height:32px">Contact us</div>

<!-- pricing -->
<h2 class="section" style="top:2630px">Select <span class="accent">service</span></h2>
<p class="abs body" style="left:230px;top:2674px;width:740px;text-align:center;font-size:11px">Choose your service. Plorvane provides a complete workstation in the Thin Client model. All you need is a monitor to get started. Both services can be encrypted using an existing PC, laptop or tablet from any location.</p>
<div class="plan" style="left:230px">
  <div class="plan-head"><span class="sq"></span><h5>Thin Client</h5><div class="price">From 99 €</div><div class="per">per user / month (from 5 users)</div></div>
  <ul>
    <li><span class="accent">✓</span>up to 5 users 115 € / month</li>
    <li><span class="accent">✓</span>Minimum term 12 months</li>
    <li><span class="accent">✓</span>Thinclient per user included</li>
    <li style="border:0"><span class="accent">✓</span>Max. 8 hours reaction time</li>
  </ul>
</div>
<div class="btn btn-line" style="left:329px;top:3123px;width:160px;height:38px">Get started now!</div>
<div class="plan" style="left:611px">
  <div class="plan-head"><span class="sq"></span><h5>Bring your own</h5><div class="price">From 75 €</div><div class="per">per user / month (from 5 users)</div></div>
  <ul>
    <li><span class="accent">✓</span>up to 5 users 85 € / month</li>
    <li><span class="accent">✓</span>No minimum term</li>
    <li><span class="accent">✓</span>Use with own terminal</li>
    <li style="border:0"><span class="accent">✓</span>Max. 8 hours reaction time</li>
  </ul>
</div>
<div class="btn btn-solid" style="left:710px;top:3123px;width:160px;height:38px">Get started now!</div>

<!-- founders -->
<h2 class="section" style="top:3232px">The <span class="accent">founders</span></h2>
<p class="abs body" style="left:160px;top:3276px;width:880px;text-align:center;font-size:11px">The company Plorvane was founded on 18.03.2019 by Henrik Almstadt and Lukas Feldhaus. The foundation was preceded by a two-year test and design phase. The headquarters of the company is located on the tranquil Seedorf.</p>
<div class="abs founder">
  <div class="abs" role="img" aria-label="Photo of a smiling founder in a suit standing in an office building" style="left:0;top:0;width:443px;height:518px;background:linear-gradient(160deg,#e6e9ec,#b8bec6 50%,#3b4656)"></div>
  <div class="abs" style="left:507px;top:60px;font-size:18px;font-weight:500">Lukas Feldhaus</div>
  <div class="abs" style="left:507px;top:106px;width:310px;border-bottom:1px solid var(--line);padding-bottom:12px;font-size:10px;color:var(--blue)">Founder and CEO</div>
  <p class="abs body" style="left:507px;top:166px;width:330px">Lukas is 45 years old, married and has two children. He has been working in IT for 19 years now and, as a trained merchant, has made a difference. In addition to his 10 years in the field of EDP design at a large electronics company, he has built up extensive knowledge in the field of IT. He is currently leading projects for medium-sized companies to migrate to the cloud.</p>
  <p class="abs body" style="left:507px;top:320px;width:330px">" My goal with Plorvane is to increase the value of IT services in the smallest companies. "</p>
  <div class="abs" style="left:507px;top:419px;width:38px;height:38px;border-radius:50%;background:var(--blue)"></div>
  <div class="abs" style="left:798px;top:432px;width:10px;height:10px;border-radius:50%;background:var(--blue)"></div>
  <div class="abs" style="left:813px;top:432px;width:10px;height:10px;border-radius:50%;border:1px solid var(--blue)"></div>
</div>

<!-- testimonials -->
<h2 class="section" style="top:3936px">What our <span class="accent">customers say</span></h2>
<div class="abs" style="left:560px;top:4004px;width:80px;height:80px;border-radius:50%;background:var(--blue)"></div>
<p class="abs" style="left:300px;top:4110px;width:600px;text-align:center;font-size:14px;font-style:italic;color:#6d737b;line-height:20px">"I'm able to work everywhere. Competitors had to file for bankruptcy after a cryptovirus. My data is safe. "</p>
<div class="abs" style="left:0;top:4176px;width:1200px;text-align:center;font-size:11px;font-weight:700;letter-spacing:1px;color:var(--blue)">HAUSVERWALTER</div>
<div class="abs" style="left:570px;top:4212px;display:flex;gap:6px">
  <span style="width:10px;height:10px;border-radius:50%;border:1px solid var(--blue)"></span><span style="width:10px;height:10px;border-radius:50%;border:1px solid var(--blue)"></span><span style="width:10px;height:10px;border-radius:50%;border:1px solid var(--blue)"></span><span style="width:10px;height:10px;border-radius:50%;border:1px solid var(--blue)"></span>
</div>

<!-- map -->
<div class="abs" role="img" aria-label="Road map of western Germany and the Netherlands with the office location marked" style="left:0;top:4303px;width:1200px;height:283px;background:linear-gradient(90deg,#a9c9ea 0,#c9dec0 30%,#d8e4c6 60%,#c6dbb8 100%)"></div>
<svg class="abs" style="left:588px;top:4420px" width="22" height="30" viewBox="0 0 22 30"><path d="M11 0a11 11 0 0 1 11 11c0 8-11 19-11 19S0 19 0 11A11 11 0 0 1 11 0z" fill="#e3342f"/><circle cx="11" cy="11" r="4" fill="#8e1b17"/></svg>

<!-- footer -->
<div class="abs footer">
  <div class="brand" style="left:80px;top:82px"><i></i>PLORVANE</div>
  <div class="social" style="left:80px"></div>
  <div class="social" style="left:120px;background:var(--blue)"></div>
  <div class="social" style="left:160px"></div>
  <div class="social" style="left:200px"></div>

  <h6 style="left:383px">Contact Us</h6>
  <div class="abs" style="left:383px;top:113px;font-size:15px;color:#fff"><span class="accent">Call Us:</span> +49 4417 5550148</div>
  <div class="abs" style="left:383px;top:140px;font-size:11px">✉ kunde@plorvane.de</div>
  <div class="abs" style="left:383px;top:174px;font-size:11px;line-height:14px"><span class="accent">Address:</span><br>Plorvane UG (haftungsbeschränkt)<br>Lindenweg 12, 27801 Seedorf</div>

  <h6 style="left:687px">Our Services</h6>
  <ul style="left:687px"><li>Express suppression</li><li>Fast programs</li><li>Professional protection</li><li>Data backup</li><li>Sustained</li><li>Predictable costs</li><li>Updates</li><li>High security</li><li>Used software</li></ul>

  <h6 style="left:915px">Quick Links</h6>
  <ul style="left:915px"><li>Home</li><li>That's How It's Done</li><li>Prices</li><li>About Us</li><li>Ask</li><li>Data Protection</li><li>Conditions</li><li>Imprint</li></ul>

  <div class="abs" style="left:80px;top:347px;width:1040px;border-top:1px solid #2f3237"></div>
  <div class="abs" style="left:80px;top:362px;font-size:10px">© 2019 <span class="accent">Plorvane</span>. All Rights Reserved</div>
  <div class="abs" style="left:1096px;top:358px;width:20px;height:20px;border-radius:50%;border:1px solid var(--blue)"></div>
</div>

</div>
</body>
</html>
```